Hair Extensions Company. Need a flyer for upcoming event.

We need a fresh new flyer to hand to customers on foot at a Mothers Day event. The flyer should include images and text. Attached is a previously made flyer which is good but could be better, this flyer is to be more in line with our Mothers Days promo. The colours/vibe in to be inline with our brand. Images will be provided that can be used.
Content that must be included
Velmora Tresses (front)
Luxury Hair Extensions
Professional Styling tools

Back can show images of the curling wands
Mention in associated with Quill Harbor somewhere on the flyer
www.velmoratresses.co.uk
Instagram icon with @velmoratresses
Instagram icon with @quillharbor
Discount code MOTHERSDAY = 50% off styling tools
Complimentary colour match email us at uk@velmoratresses.com

I can send dropbox files of HD image to use.

Please let me know if you need anymore direction.

```html
<!DOCTYPE html>
<html lang="en">
<head>
<meta charset="utf-8">
<title>Velmora Tresses – Mother's Day Flyer</title>
<link rel="stylesheet" href="https://fonts.googleapis.com/css2?family=Montserrat:wght@300;400;500&family=Oswald:wght@500&family=Kaushan+Script&display=swap">
<style>
  :root{
    --pink:#e9649c;
    --pink-soft:#f083b2;
    --blush:#f7e5df;
    --white:#ffffff;
    --stage:#3b3b3d;
    --ink-dark:#333333;
  }
  *{margin:0;padding:0;box-sizing:border-box}
  html,body{width:1200px;height:902px;overflow:hidden;background:var(--stage)}
  .canvas{position:relative;width:1200px;height:902px}
  .flyer{position:absolute;width:507px;height:711px;background:var(--white);overflow:hidden;font-family:"Montserrat",sans-serif;color:var(--pink)}
  .flyer--front{left:63px;top:80px}
  .flyer--back{left:625px;top:148px}
  .abs{position:absolute}
  .waves{position:absolute;left:0;top:0;width:507px;height:711px}
  .center-x{transform:translateX(-50%);white-space:nowrap;text-align:center}
  .script{font-family:"Kaushan Script",cursive}

  /* front */
  .portrait{left:0;top:8px;width:290px;height:400px;background:radial-gradient(ellipse at 55% 35%,#d9b9a6 0 18%,#4a302a 40%,#2c1c18 62%,#ffffff 80%)}
  .brand-ring{border:2px solid var(--pink);border-radius:50%;background:var(--white)}
  .brand-small{font-size:10px;letter-spacing:3px}
  .occasion{font-size:35px;line-height:1;white-space:nowrap;text-align:center;transform:translateX(-50%) rotate(-4deg)}
  .occasion--sub{font-size:27px;transform:translateX(-50%) rotate(-3deg)}
  .ribbon{left:254px;top:198px;width:247px;height:26px;background:var(--pink);clip-path:polygon(0 0,100% 0,97% 50%,100% 100%,0 100%,3% 50%);color:var(--white);font-size:14px;line-height:26px;text-align:center}
  .badge{left:293px;top:244px;width:180px;height:180px;border-radius:50%;background:var(--pink);border:3px solid var(--white);color:var(--white);text-align:center}
  .badge__label{margin-top:54px;font-size:13px}
  .badge__code{font-family:"Oswald",sans-serif;font-size:29px;line-height:1.1}
  .badge__rule{width:140px;margin:2px auto 3px;border-top:1.5px dashed var(--white)}
  .badge__offer{font-size:14px}
  .brand-title{font-size:40px;font-weight:500;letter-spacing:2px}
  .tagline{font-size:24px}
  .product{width:90px;height:90px;border:3px solid var(--pink);border-radius:50%;background:var(--white)}
  .product__shape{position:absolute;left:50%;top:-12px;width:14px;height:104px;transform:translateX(-50%);background:linear-gradient(#c7a58e,#222 30%,#111);border-radius:6px}
  .product__label{font-size:11px;line-height:13px;font-weight:400;width:130px}

  /* back */
  .model{top:22px;height:340px;background:radial-gradient(ellipse at 50% 30%,#e5c7ad 0 16%,#c9a471 34%,#e6d2ad 55%,#ffffff 78%)}
  .model--before{left:0;width:240px}
  .model--after{left:255px;width:252px}
  .photo-tag{font-size:11px;letter-spacing:2px;color:var(--ink-dark)}
  .brand-medium{font-size:17px;letter-spacing:5px}
  .shop-line{font-size:15.5px;font-weight:300}
  .site-script{font-size:29px}
  .handle{font-size:15.5px;display:flex;align-items:center;gap:10px}
  .handle__dot{width:22px;height:22px;border-radius:50%;background:var(--pink)}
  .info-line{font-size:15px;font-weight:300}
  .email-script{font-size:19px}
</style>
</head>
<body>
<main class="canvas">

  <!-- FRONT -->
  <section class="flyer flyer--front">
    <div class="abs portrait" role="img" aria-label="Smiling woman with long, dark, voluminous curled hair"></div>
    <svg class="waves" viewBox="0 0 507 711" aria-hidden="true">
      <path d="M0 380 C120 420 250 410 507 340 L507 360 C250 428 120 440 0 404Z" fill="var(--pink)"/>
      <path d="M0 404 C120 440 250 428 507 360 L507 711 L0 711Z" fill="var(--blush)"/>
    </svg>

    <div class="abs brand-ring" style="left:332px;top:16px;width:92px;height:92px"></div>
    <p class="abs center-x brand-small" style="left:378px;top:116px">VELMORA TRESSES</p>
    <p class="abs occasion script" style="left:380px;top:134px">Mother's Day</p>
    <p class="abs occasion occasion--sub script" style="left:372px;top:165px">&#10084; Special &#10084;</p>
    <div class="abs ribbon">www.velmoratresses.co.uk</div>

    <div class="abs badge">
      <p class="badge__label">Discount code:</p>
      <p class="badge__code">MOTHERSDAY</p>
      <div class="badge__rule"></div>
      <p class="badge__offer script">50% off styling tools</p>
    </div>

    <h1 class="abs center-x brand-title" style="left:250px;top:432px">VELMORA TRESSES</h1>
    <p class="abs center-x tagline script" style="left:244px;top:478px">Luxury Hair Extensions &amp;</p>
    <p class="abs center-x tagline script" style="left:244px;top:510px">Professional Styling tools</p>

    <div class="abs product" style="left:38px;top:567px"><div class="product__shape" role="img" aria-label="Clamp-less curling wand"></div></div>
    <div class="abs product" style="left:169px;top:567px"><div class="product__shape" role="img" aria-label="Five-in-one curling wand set" style="width:60px;height:88px;background:linear-gradient(#222,#111)"></div></div>
    <div class="abs product" style="left:285px;top:567px"><div class="product__shape" role="img" aria-label="Clamp curling wand"></div></div>
    <div class="abs product" style="left:393px;top:567px"><div class="product__shape" role="img" aria-label="Flat iron hair straightener" style="width:26px"></div></div>

    <p class="abs center-x product__label" style="left:83px;top:666px">CLAMP-LESS CURLING<br>WANDS</p>
    <p class="abs center-x product__label" style="left:214px;top:666px">5-IN-1 CURLING<br>WAND</p>
    <p class="abs center-x product__label" style="left:330px;top:666px">CLAMP WANTS</p>
    <p class="abs center-x product__label" style="left:438px;top:666px">FLAT IRON</p>
  </section>

  <!-- BACK -->
  <section class="flyer flyer--back">
    <div class="abs model model--before" role="img" aria-label="Before: woman with wavy blonde ombre hair"></div>
    <div class="abs model model--after" role="img" aria-label="After: same woman with fuller, longer blonde curled hair extensions"></div>
    <p class="abs center-x photo-tag" style="left:203px;top:28px">BEFORE</p>
    <p class="abs center-x photo-tag" style="left:438px;top:30px">AFTER</p>

    <svg class="waves" viewBox="0 0 507 711" aria-hidden="true">
      <path d="M0 348 C100 330 200 318 260 330 C330 345 430 360 507 330 L507 352 C430 385 330 372 260 360 C180 346 90 360 0 398Z" fill="var(--pink)"/>
      <path d="M0 398 C90 360 180 346 260 360 C330 372 430 385 507 352 L507 711 L0 711Z" fill="var(--blush)"/>
    </svg>

    <div class="abs brand-ring" style="left:184px;top:290px;width:138px;height:138px"></div>
    <p class="abs center-x brand-medium" style="left:250px;top:441px">VELMORA TRESSES</p>
    <p class="abs center-x shop-line" style="left:250px;top:489px">Shop Our Luxurious Hair Extensions &amp; Styling Tools</p>

    <svg class="abs" style="left:0;top:0" width="507" height="711" aria-hidden="true">
      <path d="M58 528 H54 a24 24 0 0 0 -24 24 V570 a24 24 0 0 0 24 24 H460 a24 24 0 0 0 24 -24 V552 a24 24 0 0 0 -24 -24 H448" fill="none" stroke="var(--pink)" stroke-width="1.5"/>
      <g transform="translate(242 636)" fill="none" stroke="var(--pink)" stroke-width="1.5">
        <rect x="0" y="0" width="16" height="11"/><path d="M0 0 L8 6 L16 0"/>
      </g>
    </svg>

    <p class="abs center-x site-script script" style="left:254px;top:505px">&#10084; www.velmoratresses.co.uk &#10084;</p>

    <div class="abs handle" style="left:72px;top:555px"><span class="handle__dot"></span>@velmoratresses</div>
    <div class="abs handle" style="left:280px;top:555px"><span class="handle__dot"></span>@quillharbor</div>

    <p class="abs center-x info-line" style="left:250px;top:610px">For More Information Email us</p>
    <p class="abs center-x email-script script" style="left:250px;top:654px">uk@velmoratresses.com</p>
  </section>

</main>
</body>
</html>
```